Coastal waterside shopping complex needs a billboard sign

"Harbour Verge" is the name of a building which comprises 4 shops in a coastal waterside location. We need a 2440mm (Wide) x 1100mm (High) "Harbour Verge" billboard design that will fit with the coastal theme but is modern and contemporary, positioning the building as a high class mini shopping complex.

The photo below is for reference only. We only need a design for the "Harbour Verge" sign.

The end product will need to be an EPS scalable vector file.

```html
<!DOCTYPE html>
<html lang="en">
<head>
<meta charset="utf-8">
<title>Harbour Verge</title>
<link rel="stylesheet" href="https://fonts.googleapis.com/css2?family=Poiret+One&display=swap">
<style>
  :root {
    --ocean-deep: #0f5f9c;
    --ocean-mid: #2a86b8;
    --ocean-teal: #2a9fc0;
    --foam: #dde8f3;
    --gold-face: #f1e6b4;
    --gold-light: #f7efcc;
    --gold-side: #a88d4a;
    --gold-edge: #c9ad62;
    --ghost: rgba(70, 90, 120, 0.45);
    --mark-bg: #000000;
    --mark-ink: #ffffff;
  }
  html, body {
    margin: 0;
    padding: 0;
    width: 1200px;
    height: 541px;
    overflow: hidden;
    background: var(--ocean-deep);
  }
  .billboard {
    position: relative;
    width: 1200px;
    height: 541px;
    overflow: hidden;
  }
  .seascape {
    position: absolute;
    inset: 0;
    background:
      radial-gradient(ellipse 300px 220px at 1000px 160px, rgba(236, 240, 250, 0.9), transparent 70%),
      radial-gradient(ellipse 260px 180px at 120px 340px, rgba(225, 235, 246, 0.85), transparent 70%),
      radial-gradient(ellipse 280px 140px at 560px 300px, rgba(200, 225, 240, 0.6), transparent 70%),
      radial-gradient(ellipse 320px 160px at 700px 380px, rgba(42, 170, 200, 0.7), transparent 70%),
      linear-gradient(180deg, var(--ocean-mid) 0%, #5fa2cf 45%, var(--ocean-teal) 70%, var(--ocean-deep) 100%);
  }
  .brand-mark {
    position: absolute;
    left: 560px;
    top: 0;
    width: 80px;
    height: 132px;
    background: var(--mark-bg);
    display: flex;
    align-items: center;
    justify-content: center;
    text-align: center;
  }
  .brand-mark__name {
    font-family: "Poiret One", sans-serif;
    font-weight: 400;
    font-size: 13px;
    line-height: 1.2;
    color: var(--mark-ink);
  }
  .headline {
    position: absolute;
    inset: 0;
    width: 1200px;
    height: 541px;
  }
  .headline text {
    font-family: "Poiret One", sans-serif;
    font-weight: 400;
    font-size: 205px;
    stroke-linejoin: round;
  }
  .headline__ghost { fill: var(--ghost); }
  .headline__depth { fill: var(--gold-side); stroke: var(--gold-side); stroke-width: 3; }
  .headline__face { fill: url(#goldFace); stroke: var(--gold-edge); stroke-width: 1.5; }
</style>
</head>
<body>
  <main class="billboard">
    <div class="seascape" role="img" aria-label="Breaking ocean wave with white spray under a blue sky"></div>

    <div class="brand-mark">
      <span class="brand-mark__name">Harbour<br>Verge</span>
    </div>

    <svg class="headline" viewBox="0 0 1200 541" aria-label="Harbour Verge">
      <defs>
        <linearGradient id="goldFace" x1="0" y1="0" x2="0" y2="1">
          <stop offset="0" stop-color="var(--gold-light)"/>
          <stop offset="1" stop-color="#e7d591"/>
        </linearGradient>
      </defs>
      <text class="headline__ghost" x="118" y="372" textLength="990" lengthAdjust="spacingAndGlyphs">Harbour Verge</text>
      <g class="headline__depth">
        <text x="116" y="343" textLength="990" lengthAdjust="spacingAndGlyphs">Harbour Verge</text>
        <text x="114" y="341" textLength="990" lengthAdjust="spacingAndGlyphs">Harbour Verge</text>
        <text x="112" y="339" textLength="990" lengthAdjust="spacingAndGlyphs">Harbour Verge</text>
      </g>
      <text class="headline__face" x="110" y="337" textLength="990" lengthAdjust="spacingAndGlyphs">Harbour Verge</text>
    </svg>
  </main>
</body>
</html>
```